Business card

creative business card for newly created national firm that specializes in high-density storage for retail markets. Looking for creativity and overall theme that will differentiate from others in this unique niche ...essentially a design that will provide instant recognition as we develop our identity in the marketplace. possible initial thoughts are attached with logo separately

Retail

```html
<!DOCTYPE html>
<html lang="en">
<head>
<meta charset="utf-8">
<title>Stackhaven Storage – Business Card</title>
<link rel="stylesheet" href="https://fonts.googleapis.com/css2?family=Tenor+Sans&display=swap">
<style>
  :root {
    --backdrop: #2a2a2c;
    --card: #ececec;
    --card-light: #f6f6f6;
    --slate: #6f6f71;
    --slate-dark: #5a5a5c;
    --blue: #3d95c9;
    --navy: #1f5f82;
    --ink: #3c4f5c;
    --rule: #a9a9ab;
  }
  * { box-sizing: border-box; margin: 0; padding: 0; }
  html, body { width: 1200px; height: 900px; overflow: hidden; }
  body {
    background: var(--backdrop);
    font-family: "Tenor Sans", sans-serif;
    display: flex;
    align-items: center;
    justify-content: center;
    gap: 90px;
  }
  .card {
    position: relative;
    width: 360px;
    height: 600px;
    border-radius: 22px;
    background: var(--card);
    overflow: hidden;
  }
  .card-shapes { position: absolute; inset: 0; width: 100%; height: 100%; }

  /* Front */
  .front-mark {
    position: absolute;
    left: 50%; top: 150px;
    width: 120px; height: 120px;
    margin-left: -60px;
    background: var(--blue);
  }
  .front-name {
    position: absolute;
    left: 0; right: 0; top: 385px;
    text-align: center;
    color: var(--blue);
    font-size: 33px;
    line-height: 1.15;
    letter-spacing: 0.5px;
  }
  .front-rule {
    position: absolute;
    left: 38px; right: 38px; top: 500px;
    border-top: 1px solid var(--rule);
  }
  .front-url {
    position: absolute;
    left: 0; right: 0; top: 515px;
    text-align: center;
    color: var(--slate-dark);
    font-size: 14.5px;
    letter-spacing: 0.3px;
  }

  /* Back */
  .back-brand {
    position: absolute;
    left: 0; right: 0; top: 52px;
    display: flex;
    flex-direction: column;
    align-items: center;
    gap: 14px;
  }
  .back-mark { width: 46px; height: 46px; background: var(--blue); }
  .back-name {
    color: var(--blue);
    font-size: 26px;
    text-align: center;
    line-height: 1.1;
  }
  .back-rule {
    position: absolute;
    left: 60px; right: 60px; top: 178px;
    border-top: 1px solid var(--rule);
  }
  .contact {
    position: absolute;
    left: 0; right: 0; top: 200px;
    text-align: center;
    color: var(--ink);
  }
  .person { color: var(--navy); font-size: 24px; letter-spacing: 1px; }
  .role { font-size: 12px; letter-spacing: 1px; margin-top: 4px; }
  .contact-rule { width: 200px; margin: 16px auto; border-top: 1px solid var(--rule); }
  .line { font-size: 13px; line-height: 1.45; }
  .label { font-size: 9px; letter-spacing: 1px; color: #7d8a93; margin-top: 10px; }
</style>
</head>
<body>

<article class="card card-front" aria-label="Business card front">
  <svg class="card-shapes" viewBox="0 0 360 600" aria-hidden="true">
    <polygon points="0,0 360,0 360,40 0,40" fill="var(--slate)"/>
    <polygon points="0,40 60,40 0,110" fill="var(--slate)"/>
    <polygon points="360,40 300,40 360,110" fill="var(--slate)"/>
    <rect x="0" y="320" width="360" height="22" fill="var(--slate)"/>
  </svg>
  <div class="front-mark" aria-hidden="true"></div>
  <h1 class="front-name">STACKHAVEN<br>STORAGE</h1>
  <div class="front-rule"></div>
  <p class="front-url">WWW.STACKHAVENSTORAGE.COM</p>
</article>

<article class="card card-back" aria-label="Business card back">
  <svg class="card-shapes" viewBox="0 0 360 600" aria-hidden="true">
    <polygon points="360,330 360,600 120,600" fill="var(--slate)"/>
    <polygon points="360,360 360,600 160,600" fill="var(--card-light)" opacity="0.35"/>
  </svg>
  <div class="back-brand">
    <div class="back-mark" aria-hidden="true"></div>
    <p class="back-name">STACKHAVEN<br>STORAGE</p>
  </div>
  <div class="back-rule"></div>
  <div class="contact">
    <p class="person">MARLO FENWICK</p>
    <p class="role">CEO/FOUNDER</p>
    <div class="contact-rule"></div>
    <p class="line">PO Box XXXX</p>
    <p class="line">Riverton BC, QLD, XXXX</p>
    <p class="label">PHONE</p>
    <p class="line">+ 12 987 654 321</p>
    <p class="label">EMAIL</p>
    <p class="line">mfenwick@stackhavenstorage.com</p>
  </div>
</article>

</body>
</html>
```